Handmade Soap Labels Needed for Local Soap Supplier

I am rebranding my Handmade Soap Business and require New Handmade Soap Labels. I made the current labels on word and they need a fresh new look for the new business name. I live in Fremantle, Western Australia and the culture is very environmentally friendly and supports local products. The final design would need to be simple but eye catching. There are 16 soap varieties at the moment so I would need to be able to edit the labels to update ingredients etc for new soap varieties. I have attached my current label for you to see what I currently have. The business name is also changing so I have included the new logo which is needed on the new labels.

Requirements
Must have
• Must have logo, name of the soap eg. Lavender
• Soap ingredients
• Handmade
Nice to have
• Design that is eye catching and would make a great gift
Should not have
• Should not be too busy

```html
<!DOCTYPE html>
<html lang="en">
<head>
<meta charset="utf-8">
<title>Willow &amp; Wren Soap Co. – Soap Label</title>
<link rel="stylesheet" href="https://fonts.googleapis.com/css2?family=Montserrat:ital,wght@0,400;0,500;0,600;1,400&display=swap">
<style>
  :root {
    --paper: #ffffff;
    --ink: #1a1a1a;
    --band-green: #2e8a08;
    --frame-green: #4fae2b;
    --band-text: #ffffff;
  }
  * { margin: 0; padding: 0; box-sizing: border-box; }
  html, body { width: 1200px; height: 288px; overflow: hidden; background: var(--paper); }
  body { font-family: "Montserrat", Arial, sans-serif; color: var(--ink); }

  .label { position: relative; width: 1200px; height: 288px; background: var(--paper); }

  /* Ingredients panel */
  .ingredients { position: absolute; left: 34px; top: 55px; width: 250px; }
  .ingredients__title { font-size: 16px; font-weight: 500; letter-spacing: 0.3px; margin-bottom: 8px; }
  .ingredients__list { font-size: 11.6px; line-height: 21.2px; letter-spacing: 0.4px; text-transform: uppercase; padding-left: 1px; }

  /* Vertical bands */
  .band {
    position: absolute; top: 0; height: 288px; width: 53px;
    background: var(--band-green);
    display: flex; align-items: center; justify-content: center;
  }
  .band--left { left: 313px; }
  .band--right { left: 834px; }
  .band__text {
    color: var(--band-text); font-size: 13.6px; letter-spacing: 0.6px;
    white-space: nowrap; text-transform: uppercase;
  }
  .band--left .band__text { writing-mode: vertical-rl; }
  .band--right .band__text { writing-mode: vertical-rl; transform: rotate(180deg); }
  .band__gap { display: inline-block; width: 8px; }

  /* Centre panel */
  .brand-panel {
    position: absolute; left: 419px; top: 26px; width: 361px; height: 235px;
    border: 1.6px solid var(--frame-green); border-radius: 22px;
    text-align: center;
  }
  .brand-panel__kicker { position: absolute; top: 33px; width: 100%; font-size: 13.6px; letter-spacing: 0.5px; }
  .brand-panel__name {
    position: absolute; top: 98px; width: 100%;
    font-size: 21px; font-weight: 400; letter-spacing: 1.5px; text-transform: uppercase;
  }
  .brand-panel__name-sub { display: block; font-size: 10.5px; letter-spacing: 2px; margin-top: 14px; }
  .brand-panel__tagline { position: absolute; top: 194px; width: 100%; font-size: 12.8px; font-style: italic; letter-spacing: 0.6px; }

  /* Story & contact panel */
  .story { position: absolute; left: 945px; top: 57px; width: 240px; }
  .story__text { font-size: 11.6px; line-height: 21.2px; letter-spacing: 0.4px; text-transform: uppercase; }
  .location { margin-top: 15px; }
  .location__city { font-size: 16px; font-weight: 600; letter-spacing: 5.4px; line-height: 20px; }
  .location__region { font-size: 12.8px; letter-spacing: 1.1px; line-height: 18px; }
  .contact { margin-top: 13px; }
  .contact__row { display: flex; align-items: center; height: 24px; }
  .contact__icon { width: 13px; height: 13px; margin-right: 14px; fill: var(--ink); }
  .contact__phone { font-size: 13.6px; font-weight: 500; letter-spacing: 1.8px; }
  .contact__email { font-size: 11.2px; letter-spacing: 1.4px; }
</style>
</head>
<body>
<main class="label">

  <section class="ingredients">
    <h2 class="ingredients__title">INGREDIENTS</h2>
    <p class="ingredients__list">Purified water, olive oil, coconut oil, rice bran oil, sunflower oil, organic shea butter, sodium hydroxide, yellow Brazilian clay, orange essential oil &amp; calendula petals</p>
  </section>

  <div class="band band--left"><span class="band__text">100%<span class="band__gap"></span>Sustainable</span></div>

  <section class="brand-panel">
    <p class="brand-panel__kicker">TRADITIONAL HANDCRAFTED SOAP</p>
    <h1 class="brand-panel__name">Willow &amp; Wren<span class="brand-panel__name-sub">Soap Co.</span></h1>
    <p class="brand-panel__tagline">HAND MADE WITH LOVE</p>
  </section>

  <div class="band band--right"><span class="band__text">Rich Generous Lather</span></div>

  <section class="story">
    <p class="story__text">Each batch is hand made in<br>my kitchen. Cut by hand,<br>then cured for 4weeks<br>for you to enjoy.</p>
    <div class="location">
      <p class="location__city">FREMANTLE</p>
      <p class="location__region">WESTERN AUSTRALIA</p>
    </div>
    <div class="contact">
      <p class="contact__row">
        <svg class="contact__icon" viewBox="0 0 24 24" aria-hidden="true"><path d="M6.6 10.8a15.1 15.1 0 0 0 6.6 6.6l2.2-2.2a1 1 0 0 1 1-.25 11.4 11.4 0 0 0 3.6.57 1 1 0 0 1 1 1V20a1 1 0 0 1-1 1A17 17 0 0 1 3 4a1 1 0 0 1 1-1h3.5a1 1 0 0 1 1 1c0 1.25.2 2.45.57 3.57a1 1 0 0 1-.25 1z"/></svg>
        <span class="contact__phone">0400 512 768</span>
      </p>
      <p class="contact__row">
        <svg class="contact__icon" viewBox="0 0 24 24" aria-hidden="true"><path d="M2 5h20v14H2z M3.5 6.5 12 13l8.5-6.5" fill="none" stroke="#1a1a1a" stroke-width="0"/><path d="M2 5h20L12 12.5z"/><path d="M2 6.8v12.2h20V6.8l-10 7.6z"/></svg>
        <span class="contact__email">hello@willowwren.au</span>
      </p>
    </div>
  </section>

</main>
</body>
</html>
```